Dentistry

Dentist's personal business card. No logo needed. The card shoul deliver the massage of reliability, professionalism, experience.
Please ad the full brief of the project: down the line it says: the winning look should be precise and pristine NO pictures of Teeth, smiles, instruments etc.

The details to be desplaid are:
Dr. Rob Valdoni
Doctor of Dental Surgery
PHD
Web. Www.drvaldoni.com
Email. Rob@drvaldoni.com
Tel 07731482590
Surgery address. 27Bharwick road London SW4 7QN UK
82 Fenwyn Row London SW3 2HT. Uk

Reason: Decided to make the payment unrefundable in order to get more designers involved.

Requirements
Should not have
• Logo, teeth, smile any sort of instruments.

```html
<!DOCTYPE html>
<html lang="en">
<head>
<meta charset="utf-8">
<title>Dr. Rob Valdoni – Business Card Back</title>
<link rel="stylesheet" href="https://fonts.googleapis.com/css2?family=Exo+2:wght@300;400&display=swap">
<style>
  :root {
    --card-navy: #16123a;
    --accent-blue: #0a7cc4;
    --text-white: #ffffff;
  }
  html, body {
    margin: 0;
    padding: 0;
    width: 1200px;
    height: 777px;
    overflow: hidden;
    background: #ffffff;
  }
  .card {
    position: relative;
    width: 1200px;
    height: 777px;
    background: var(--card-navy);
    border-radius: 48px;
    overflow: hidden;
    font-family: "Exo 2", "Segoe UI", sans-serif;
    font-weight: 300;
    color: var(--text-white);
  }
  .icon-rail {
    position: absolute;
    left: 150px;
    top: 141px;
    width: 70px;
    height: 495px;
    background: var(--accent-blue);
    border-radius: 12px;
  }
  .icon {
    position: absolute;
    left: 167px;
    width: 36px;
    height: 36px;
  }
  .icon--phone { top: 156px; }
  .icon--mail  { top: 218px; }
  .icon--web   { top: 281px; }
  .icon--pin   { top: 400px; }
  .contact-line {
    position: absolute;
    left: 267px;
    margin: 0;
    font-size: 41px;
    line-height: 1;
    letter-spacing: 0.3px;
    white-space: nowrap;
  }
  .contact-line--phone   { top: 147px; }
  .contact-line--email   { top: 211px; }
  .contact-line--web     { top: 275px; }
  .contact-line--label   { top: 404px; }
  .contact-line--surgery { top: 476px; }
  .contact-line--second  { top: 583px; }
  .divider {
    position: absolute;
    left: 266px;
    width: 784px;
    height: 4px;
    background: var(--accent-blue);
  }
  .divider--upper { top: 368px; }
  .divider--lower { top: 552px; }
</style>
</head>
<body>
  <div class="card">
    <div class="icon-rail"></div>

    <svg class="icon icon--phone" viewBox="0 0 36 36" fill="none" stroke="#fff" stroke-width="2.4">
      <circle cx="18" cy="18" r="15.5"/>
      <path d="M14 9.5 h3 v5 h-2.2 v7 h2.2 v5 h-3 c-1.5 0 -2.5 -3.5 -2.5 -8.5 s1 -8.5 2.5 -8.5z" fill="#fff" stroke="none"/>
    </svg>

    <svg class="icon icon--mail" viewBox="0 0 36 36" fill="none" stroke="#fff" stroke-width="2">
      <rect x="3" y="8" width="30" height="20"/>
      <path d="M3 8 L18 20 L33 8 M3 28 L14 17 M33 28 L22 17"/>
    </svg>

    <svg class="icon icon--web" viewBox="0 0 36 36">
      <circle cx="18" cy="18" r="16" fill="#fff"/>
      <path d="M9 8 c4 1 6 3 5 6 c-1 3 -5 2 -5 6 c0 3 3 4 3 8 c-4 -2 -8 -6 -8 -11 c0 -4 2 -7 5 -9z M22 4.5 c2 2 1 4 3 5 s4 0 5 3 c1 3 -2 4 -4 5 c-2 1 -1 5 -3 8 c-2 2 -4 -1 -4 -4 c0 -3 -3 -3 -3 -6 s4 -3 4 -6 s-1 -4 2 -5z" fill="var(--accent-blue)"/>
    </svg>

    <svg class="icon icon--pin" viewBox="0 0 36 36" fill="none" stroke="#fff" stroke-width="2.2">
      <path d="M18 33 C12 25 7 19 7 13 a11 11 0 0 1 22 0 c0 6 -5 12 -11 20z"/>
      <circle cx="18" cy="13" r="5"/>
    </svg>

    <p class="contact-line contact-line--phone">07731482590</p>
    <p class="contact-line contact-line--email">rob@drvaldoni.com</p>
    <p class="contact-line contact-line--web">www.drvaldoni.com</p>

    <div class="divider divider--upper"></div>

    <p class="contact-line contact-line--label">Surgery address:</p>
    <p class="contact-line contact-line--surgery">27Bharwick road London SW4 7QN UK</p>

    <div class="divider divider--lower"></div>

    <p class="contact-line contact-line--second">82 Fenwyn Row London SW3 2HT. Uk</p>
  </div>
</body>
</html>
```